Package Design for Plant-based Dumplings

We need a CPG Package design for a new product we're launching. I included example (front and back) of what a typical information food package has, so you can use it as reference.

Target Market(s)

Consumers that are seeking non-meat items. Environment concerned consumers.

Colors

Designer to choose colors to be used in the design.

Requirements
Must have
• Modern and clean looking design.
Nice to have
• might have multiple flavors, so make design where it could be have multiple variations.

```html
<!DOCTYPE html>
<html lang="en">
<head>
<meta charset="utf-8">
<title>MeiRose Foods – Plant-Based Dumplings Package</title>
<link rel="stylesheet" href="https://fonts.googleapis.com/css2?family=Roboto:wght@400;500;700;900&display=swap">
<style>
  :root {
    --orange: #f7461b;
    --ink: #111111;
    --stone-dark: #1e1f21;
    --stone-mid: #3a3b3e;
    --white: #ffffff;
    --line: #444444;
  }
  * { box-sizing: border-box; margin: 0; padding: 0; }
  html, body { width: 1200px; height: 832px; overflow: hidden; background: var(--white); }
  body { font-family: "Roboto", Arial, sans-serif; color: var(--ink); position: relative; }

  .panel { position: absolute; top: 29px; width: 544px; height: 762px; border: 1px solid #555; overflow: hidden; }
  .panel--front { left: 52px; background: var(--stone-dark); }
  .panel--back { left: 613px; background: var(--white); }

  /* Front */
  .product-photo {
    position: absolute; inset: 0;
    background: radial-gradient(ellipse at 52% 55%, #c9a46a 0%, #8b6c44 18%, #2b2b2d 38%, var(--stone-mid) 60%, var(--stone-dark) 100%);
  }
  .front-waves { position: absolute; inset: 0; }
  .brand { position: absolute; }
  .brand__name { font-weight: 900; font-size: 44px; line-height: 0.95; letter-spacing: 0.5px; }
  .panel--front .brand { left: 109px; top: 46px; }
  .panel--front .brand__name { color: var(--white); }

  .title-band { position: absolute; left: 0; top: 166px; width: 445px; height: 81px; background: rgba(20,20,20,0.85); border-radius: 0 8px 8px 0; }
  .title-badge { position: absolute; left: 0; top: 179px; width: 400px; height: 83px; background: var(--orange); border-radius: 0 6px 6px 0; padding: 9px 0 0 14px; }
  .title-badge h1 { color: var(--white); font-weight: 700; font-size: 34.5px; letter-spacing: 0.3px; line-height: 1.05; }
  .title-badge p { color: var(--ink); font-weight: 700; font-size: 20px; margin-top: 3px; margin-left: 5px; }

  .net-weight { position: absolute; left: 13px; bottom: 10px; font-weight: 700; font-size: 17px; line-height: 23px; color: var(--ink); }
  .claims { position: absolute; right: 13px; bottom: 14px; text-align: right; color: var(--white); font-weight: 700; font-size: 23px; line-height: 23px; }

  /* Back */
  .panel--back .brand { left: 82px; top: 44px; }
  .panel--back .brand__name { color: var(--ink); font-size: 46px; }
  .story { position: absolute; left: 21px; top: 151px; width: 500px; font-weight: 500; font-size: 14.4px; line-height: 22.6px; }
  .ingredients { position: absolute; left: 21px; top: 313px; width: 322px; font-size: 7.5px; font-weight: 700; line-height: 14.9px; text-transform: uppercase; }
  .ingredients p + p { margin-top: 14.9px; }
  .ingredients .allergens { text-transform: none; }
  .heating { position: absolute; left: 21px; top: 566px; width: 360px; font-size: 7px; font-weight: 700; line-height: 14.9px; }
  .heating h2 { font-size: 7px; font-weight: 700; }

  .nutrition { position: absolute; left: 356px; top: 311px; width: 155px; height: 281px; border: 1px solid var(--ink); padding: 3px 5px; font-size: 6.3px; }
  .nutrition h2 { font-size: 18px; font-weight: 700; line-height: 18px; border-bottom: 1px solid var(--ink); padding-bottom: 2px; }
  .nutrition .servings { font-size: 7.4px; line-height: 9px; }
  .nutrition .size { display: flex; justify-content: space-between; font-weight: 700; font-size: 7.8px; border-bottom: 6px solid var(--ink); padding-bottom: 2px; }
  .nutrition .amount { font-size: 5px; font-weight: 700; margin-top: 3px; }
  .nutrition .calories { display: flex; justify-content: space-between; align-items: flex-end; font-weight: 700; border-bottom: 3px solid var(--ink); line-height: 15px; }
  .nutrition .calories span:first-child { font-size: 13px; }
  .nutrition .calories span:last-child { font-size: 18px; }
  .nutrition .dv { text-align: right; font-size: 5px; font-weight: 700; border-bottom: 1px solid var(--line); padding: 2px 0 1px; }
  .nutrition .row { display: flex; justify-content: space-between; border-bottom: 1px solid var(--line); line-height: 10.2px; }
  .nutrition .row b { font-weight: 700; }
  .nutrition .row span:last-child { font-weight: 700; }
  .nutrition .row--thick { border-bottom: 5px solid var(--ink); }
  .nutrition .row--med { border-bottom: 3px solid var(--ink); }
  .nutrition .note { font-size: 4.4px; line-height: 6px; margin-top: 3px; }

  .barcode-label { position: absolute; left: 382px; top: 598px; font-weight: 700; font-size: 12px; text-align: center; width: 120px; }
  .barcode-box { position: absolute; left: 374px; top: 619px; width: 137px; height: 71px; border: 1px solid var(--ink); display: flex; align-items: center; justify-content: center; font-weight: 500; font-size: 12px; }
  .maker { position: absolute; right: 28px; top: 706px; text-align: right; font-size: 7px; font-weight: 700; line-height: 15px; }
</style>
</head>
<body>

<section class="panel panel--front" aria-label="Package front">
  <div class="product-photo" role="img" aria-label="Photo of pan-fried plant-based dumplings with sesame seeds in a cast iron skillet on dark stone, chopsticks at top"></div>

  <svg class="front-waves" viewBox="0 0 544 762" width="544" height="762" aria-hidden="true">
    <path d="M0,262 L62,262 C30,385 70,550 200,640 C310,710 450,640 544,530 L544,762 L0,762 Z" fill="var(--white)"/>
    <path d="M0,262 L48,262 C18,390 62,565 200,658 C320,730 460,670 544,550 L544,762 L0,762 Z" fill="var(--orange)"/>
    <path d="M62,262 C30,385 70,550 200,640 C310,710 450,640 544,530" fill="none" stroke="var(--ink)" stroke-width="1" stroke-dasharray="3 3" opacity="0.6"/>
    <path d="M48,285 C22,405 66,570 205,666 C330,735 465,675 544,564" fill="none" stroke="var(--white)" stroke-width="1" stroke-dasharray="3 3"/>
  </svg>

  <div class="brand">
    <span class="brand__name">MeiRose<br>Foods</span>
  </div>

  <div class="title-band"></div>
  <div class="title-badge">
    <h1>Plant-Based Dumplings</h1>
    <p>Using Plant-based Meat and Vegetables</p>
  </div>

  <div class="net-weight">Net Wt. 2 LBs (32oz)<br>Keep Frozen</div>
  <div class="claims">Vegan<br>Ready in Minutes<br>No Soy<br>20g of Protein</div>
</section>

<section class="panel panel--back" aria-label="Package back">
  <div class="brand">
    <span class="brand__name">MeiRose<br>Foods</span>
  </div>

  <p class="story">The brand name MeiRose Foods was inspired from a lady named Mei Rose that started a food business in S. Korea during the 1950s. Mei’s family immigrated to the U.S. in late 1990s and the Rose family began making dumplings out-of-their home kitchen and sold into local markets.&nbsp; Business grew and the family eventually built a state-of-the-art USDA food factory in 2003.&nbsp; Dumplings made at MeiRose’s factory is now available throughout retailers in US and Canada.</p>

  <div class="ingredients">
    <p>Ingredient List<br>Filling: Plant-based meat(water, pea protein isolate,canola and sunflower oil, rice flour, spice, tomato powder,contains 0.5% or less: yeast extract, sugar, potassium chloride,tapioca maltodextrin, citric acid, salt, acacia gum, onion extract,natural flavor, garlic extract ), cabbage, onion, sweet potato noodle(water, sweet potato starch), green onion, seasoning(onion powder, grilled flavor, sugar, garlic dehydrated, spice,natural flavor, yeast extract), carrot, water, starch (cornstarch,modified starch), sesame oil,&nbsp; canola oil, garlic.</p>
    <p>Dough:wheat flour enriched([niacin, reduced iron, thiamine mononitrate, riboflavin, folic acid] malted barley flour),water, conditioner(tapioca starch, salt, dextrose, potassium chloride, monoglycerides, modified cellulose gum, xanthan gum),canola oil.</p>
    <p class="allergens">Allergens: Wheat</p>
  </div>

  <div class="heating">
    <h2>Heating Instructions</h2>
    <p>Steam:</p>
    <p>1. Remove frozen dumplings from the package and place them in a steamer over boiling water.</p>
    <p>2. Cover the steamer approximately 8-10 minutes or until cooked thoroughly.</p>
    <p>Pan Fry:</p>
    <p>1. Heat 2 teaspoons of oil in frying pan. Carefully place thawed dumplings into heated pan.</p>
    <p>2. Heat approximately 3-4 minutes or until golden brown.</p>
    <p>Microwave:</p>
    <p>1. Place frozen dumplings on microwave-safe dish.</p>
    <p>2. Cover with damp paper towel and heat on high for 2 to 3 minutes or until hot.</p>
  </div>

  <div class="nutrition">
    <h2>Nutrition Facts</h2>
    <div class="servings">about 8 servings per container</div>
    <div class="size"><span>Servings Size</span><span>3 pieces (90g)</span></div>
    <div class="amount">Amount per serving</div>
    <div class="calories"><span>Calories</span><span>180</span></div>
    <div class="dv">% Daily Value</div>
    <div class="row"><span><b>Total Fat</b> 8g</span><span>10%</span></div>
    <div class="row"><span>Saturdated Fat 2.5g</span><span>13%</span></div>
    <div class="row"><span>Trans&nbsp;&nbsp;&nbsp; Fat 0g</span><span></span></div>
    <div class="row"><span><b>Cholesterol</b> 15mg</span><span>5%</span></div>
    <div class="row"><span><b>Sodium</b> 410mg</span><span>18%</span></div>
    <div class="row"><span><b>Total Carbohydrate</b> 19g</span><span>7%</span></div>
    <div class="row"><span>Dietary Fiber 1g</span><span>4%</span></div>
    <div class="row"><span>Total Sugars 2g</span><span></span></div>
    <div class="row"><span>Includes 1g Added Sugars</span><span>2%</span></div>
    <div class="row row--thick"><span><b>Protein</b> 8g</span><span></span></div>
    <div class="row"><span>Vitamin D&nbsp; 0mcg</span><span>0%</span></div>
    <div class="row"><span>Calcium 30mg</span><span>2%</span></div>
    <div class="row"><span>Iron 1.2mg</span><span>6%</span></div>
    <div class="row row--med"><span>Potassium 176mg</span><span>4%</span></div>
    <p class="note">* The % Daily Value tells you how much a nutrient in a serving of food contributes to a daily diet. 2000 calories a day is used for general nutrition advise.</p>
  </div>

  <div class="barcode-label">Barcode:</div>
  <div class="barcode-box">place-holder for now</div>

  <div class="maker">Manufactured For:<br>Harbor Pantry Co.<br>Oakridge, CA 94000</div>
</section>

</body>
</html>
```